Hero Image Redesign for TRIL Consulting Website

About us:
TRIL Consulting is an organisational psychology and human resource management consulting firm based in Melbourne, Australia (www.trilconsult.com.au). We are a B2B offering a range of organisational psychology measurement and consulting. The largest part of our business is our online psychometric assessments, which are self-managed via an online portal, which is currently used by many organisations worldwide as part of their recruitment process.

What we are looking for:
We are seeking assistance to redesign an image located above the fold - on the top right hand side of homepage. We want an image of a small group of diverse people happily working together using a laptop (either individually or as a group), overlayed with graphic representations reflective of using our online Psychometric Assessment tool, in an interactive fashion.

The graphics will highlight key features of the self-service TRIL Psychometric Assessment Portal, specifically ease of use, flexibility and our integrated approach. We want the image to look clean, clear, minimal, with use of negative space. All graphics must be accessible (including sufficient colour contrast and text size).

We would like the graphic to feature 3 “pop ups” highlighting features, and these should appear over the image:

1. Setup participants easily online
2. Check the status of an assessment
3. View participants’ reports

Examples from other SaaS websites attached.

The final design should communicate trust, reliability, our scientific evidence based approach, and our approachable and friendly customer service.

Our main brand colours are:
• Navy – HEX #2F2971
• Mid Blue – HEX #0C75C0
• Black – HEX #000000

About TRIL’ website and potential for future work:

• TRIL’ website pages have been created using Bricks Builder for WordPress.
• There is a strong possibility of future projects following successful delivery. We are an excellent client – ethical, professional and with a genuine commitment to partnership.

Need extra days to review

```html
<!DOCTYPE html>
<html lang="en">
<head>
<meta charset="utf-8">
<title>TRIL Consulting – Organisational Psychology Consulting</title>
<link rel="stylesheet" href="https://fonts.googleapis.com/css2?family=Lexend:wght@500;600&family=Plus+Jakarta+Sans:wght@400;500;600;700&family=Open+Sans:wght@700&display=swap">
<style>
  :root {
    --navy: #2f2971;
    --ink: #2b2b33;
    --body: #3c3c46;
    --teal: #a6e6df;
    --teal-soft: #c4efea;
    --lavender: #dcd9ec;
    --nav-bg: #f4f4f5;
    --white: #ffffff;
    --rule: #d6d6da;
  }
  * { box-sizing: border-box; margin: 0; padding: 0; }
  html, body { width: 1200px; height: 625px; overflow: hidden; background: var(--white); }
  body { position: relative; font-family: "Plus Jakarta Sans", sans-serif; color: var(--ink); }

  .site-header {
    position: absolute; left: 0; top: 26px; width: 1200px; height: 57px;
    background: var(--nav-bg); display: flex; align-items: center;
  }
  .brand {
    position: absolute; left: 52px; display: flex; align-items: center; gap: 8px;
    font-family: "Plus Jakarta Sans", sans-serif; font-weight: 700; font-size: 21px; color: var(--navy);
  }
  .brand-mark { width: 20px; height: 20px; background: var(--teal); border-radius: 4px; }
  .main-nav { position: absolute; left: 336px; display: flex; gap: 0; font-size: 12px; font-weight: 500; color: var(--ink); }
  .main-nav span { display: inline-flex; align-items: center; gap: 7px; }
  .main-nav svg { width: 9px; height: 6px; }
  .nav-1 { position: absolute; left: 0; white-space: nowrap; }

  .hero-title {
    position: absolute; left: 83px; top: 136px;
    font-family: "Lexend", sans-serif; font-weight: 600; font-size: 53px; line-height: 61px;
    color: var(--navy); letter-spacing: -0.3px;
  }
  .hero-copy {
    position: absolute; left: 84px; top: 351px; width: 470px;
    font-size: 19.5px; line-height: 34px; color: var(--body); letter-spacing: -0.3px;
  }
  .btn {
    position: absolute; top: 465px; height: 46px; display: flex; align-items: center; justify-content: center;
    font-size: 13.5px; font-weight: 700; border-radius: 3px; box-shadow: 0 3px 6px rgba(0,0,0,0.12);
  }
  .btn-primary { left: 84px; width: 178px; background: var(--navy); color: var(--white); }
  .btn-secondary { left: 293px; width: 179px; background: var(--teal); color: var(--navy); gap: 8px; font-weight: 600; }

  .deco-circle { position: absolute; left: 1042px; top: 95px; width: 130px; height: 130px; border-radius: 50%; background: var(--teal-soft); }
  .deco-block { position: absolute; left: 877px; top: 346px; width: 248px; height: 239px; border-radius: 18px; background: var(--lavender); }
  .hero-photo {
    position: absolute; left: 636px; top: 140px; width: 477px; height: 431px; border-radius: 20px;
    background: linear-gradient(135deg, #c9c6c2 0%, #e4e2df 40%, #f1f0ee 70%, #d8d9dc 100%);
  }

  .feature-card {
    position: absolute; width: 274px; height: 76px; border-radius: 6px;
    background: rgba(255,255,255,0.93); box-shadow: 0 2px 8px rgba(0,0,0,0.08);
    display: flex; align-items: center; gap: 18px; padding-left: 17px;
  }
  .feature-card svg { width: 40px; height: 40px; flex: none; }
  .feature-card p { font-family: "Open Sans", sans-serif; font-weight: 700; font-size: 21px; line-height: 24px; color: var(--navy); }
  .card-setup { left: 457px; top: 231px; }
  .card-status { left: 563px; top: 329px; }
  .card-reports { left: 649px; top: 438px; }

  .page-rule { position: absolute; left: 0; top: 623px; width: 1200px; height: 1px; background: var(--rule); }
</style>
</head>
<body>
  <header class="site-header">
    <div class="brand"><span class="brand-mark"></span>TRIL Consulting</div>
    <nav class="main-nav">
      <span style="position:absolute;left:0;white-space:nowrap">Psychometric testing <svg viewBox="0 0 9 6"><path d="M1 1l3.5 3.5L8 1" fill="none" stroke="#2b2b33" stroke-width="1.4"/></svg></span>
      <span style="position:absolute;left:152px;white-space:nowrap">Employee wellbeing <svg viewBox="0 0 9 6"><path d="M1 1l3.5 3.5L8 1" fill="none" stroke="#2b2b33" stroke-width="1.4"/></svg></span>
      <span style="position:absolute;left:300px;white-space:nowrap">HR consulting <svg viewBox="0 0 9 6"><path d="M1 1l3.5 3.5L8 1" fill="none" stroke="#2b2b33" stroke-width="1.4"/></svg></span>
      <span style="position:absolute;left:413px;white-space:nowrap">Events</span>
      <span style="position:absolute;left:472px;white-space:nowrap">Knowledge hub <svg viewBox="0 0 9 6"><path d="M1 1l3.5 3.5L8 1" fill="none" stroke="#2b2b33" stroke-width="1.4"/></svg></span>
      <span style="position:absolute;left:595px;white-space:nowrap">About us <svg viewBox="0 0 9 6"><path d="M1 1l3.5 3.5L8 1" fill="none" stroke="#2b2b33" stroke-width="1.4"/></svg></span>
      <span style="position:absolute;left:683px;white-space:nowrap">Contact</span>
    </nav>
  </header>

  <h1 class="hero-title">Organisational<br>Psychology<br>Consulting</h1>
  <p class="hero-copy">Optimise your workforce with psychometric testing, engagement surveys, wellbeing measures, and organisational development.</p>
  <a class="btn btn-primary">Psychometric Testing</a>
  <a class="btn btn-secondary">Speak to an Expert <svg width="10" height="10" viewBox="0 0 10 10"><path d="M1 5h7M5 2l3 3-3 3" fill="none" stroke="#2f2971" stroke-width="1.5"/></svg></a>

  <div class="deco-circle"></div>
  <div class="deco-block"></div>
  <div class="hero-photo" role="img" aria-label="Photo of a diverse group of colleagues smiling while working together at laptops in a bright office"></div>

  <div class="feature-card card-setup">
    <svg viewBox="0 0 40 40" fill="none" stroke="#2f2971" stroke-width="1.3">
      <circle cx="20" cy="20" r="11"/><circle cx="20" cy="20" r="3"/>
      <path d="M20 9v8M20 23v8M9 20h8M23 20h8" stroke="#7fcfc5"/>
      <circle cx="20" cy="5" r="2.5"/><circle cx="20" cy="35" r="2.5"/><circle cx="5" cy="20" r="2.5"/><circle cx="35" cy="20" r="2.5" stroke="#7fcfc5"/>
    </svg>
    <p>Setup participants easily online</p>
  </div>
  <div class="feature-card card-status">
    <svg viewBox="0 0 40 40" fill="none" stroke="#2f2971" stroke-width="1.3">
      <rect x="3" y="8" width="34" height="24" rx="2"/><path d="M1 35h38" />
      <path d="M7 22h10M7 26h14" stroke="#7fcfc5"/>
      <circle cx="15" cy="12" r="6"/><path d="M19 16l4 4"/>
      <circle cx="30" cy="21" r="2.5"/><path d="M26 28c0-3 8-3 8 0"/>
    </svg>
    <p>Check the status of an assessment</p>
  </div>
  <div class="feature-card card-reports">
    <svg viewBox="0 0 40 40" fill="none" stroke="#2f2971" stroke-width="1.3">
      <rect x="7" y="4" width="22" height="30" rx="2"/><rect x="4" y="7" width="22" height="30" rx="2"/>
      <path d="M8 16l4-4 4 3 5-5" stroke="#7fcfc5"/><path d="M8 24h8M8 28h6"/>
      <path d="M20 27c3-5 13-5 16 0c-3 5-13 5-16 0z" stroke="#7fcfc5"/><circle cx="28" cy="27" r="2.5"/>
    </svg>
    <p>View participants’ reports</p>
  </div>

  <div class="page-rule"></div>
</body>
</html>
```